Luxury Eye Cream Label

Velmora Skin is developing a line of luxury dermatology creams designed to improve and treat various skin conditions and esthetic problems.
All creams are handmade by registered pharmacies according to patient needs, on the same day of the order. (meaning the creams are not premade. the creams are freshly made without any preservatives or stabilizers.)
The labels are two. One for the upper lid of an aluminum container 4.0 cm. in diameter containing company logo and description of the cream. The other one is for the bottom of the container 4.0 in diameter containing pharmacy information.
The label should convey professional, MD, and luxury feel.
(Upper Lid Label)
Logo of velmora skin
EYE CARE CREAM - intensive
Doctor Series
handmade . Doctor formulated . registered Pharmacy . highest ethical standards . (in a circular pattern on the label)
Ingredients: Marigold extract, Witch Hazel Distillate, Water, Glycerin, Stearyl Alcohol, Wheat Germ Oil, Polysorbate 60, Sesame Oil, Myristyl Myristate, Cetyl Alcohol, Sorbitan Stearate, Phenoxyethanol, Calendula Extract, Cornflower Extract, Sodium Alginate, Sodium Citrate, Mica, Vit. C, Vit. E.
Please, adhere to the above content, and dimension of the label of 4 cm in diameter. Also, please view it to scale. This is a relatively small container, aluminum ½ ounce (15ml) cream.
The Bottom of the Jar will have a label with the following information. This is obligatory, because of regulatory requirements for any product prepared by a pharmacy.
I understand that the space is limited. The background should be a lighter color, and the pharmacist will hand write the information (with a darker color marker).
EXTERNAL USE
Pharmacy: Pelaro, 18 Blvd. Ts. Orlinov, Sofia 1157, ph. 02 9473615
Rx No. Date
Patient Name age
Pharmacist Good until:
Please, view it to scale of 4 cm in diameter (which is the actual label of the Face Cream Intense), so you will have a better feeling of the design.
Thank you so much.

```html
<!DOCTYPE html>
<html lang="en">
<head>
<meta charset="utf-8">
<title>Velmora Skin — Intensive Eye Care Cream Labels</title>
<link rel="stylesheet" href="https://fonts.googleapis.com/css2?family=Anton&family=Arimo:wght@400;700&display=swap">
<style>
  :root {
    --page: #ffffff;
    --ink: #000000;
    --ink-soft: #3a3a3a;
    --die-line: #e4e4e8;
  }
  html, body {
    margin: 0;
    padding: 0;
    width: 1200px;
    height: 1200px;
    overflow: hidden;
    background: var(--page);
  }
  .sheet {
    position: relative;
    width: 1200px;
    height: 1200px;
  }
  .label {
    position: absolute;
    width: 530px;
    height: 530px;
  }
  .label--lid-a { left: 55px; top: 45px; }
  .label--base-a { left: 615px; top: 45px; }
  .label--lid-b { left: 55px; top: 625px; }
  .label--base-b { left: 615px; top: 625px; }

  .die-cut { fill: var(--page); stroke: var(--die-line); stroke-width: 1.2; }
  .rule { stroke: var(--ink); stroke-width: 2; }

  .claim { font-family: "Arimo", Arial, sans-serif; font-weight: 700; font-size: 18px; fill: var(--ink); }
  .brand-name { font-family: "Arimo", Arial, sans-serif; font-weight: 700; font-size: 25px; fill: var(--ink); letter-spacing: 0.3px; }
  .series { font-family: "Arimo", Arial, sans-serif; font-size: 21px; fill: var(--ink-soft); }
  .product-name { font-family: "Anton", "Arial Narrow", sans-serif; font-size: 47px; fill: var(--ink); letter-spacing: 0.5px; }
  .product-type { font-family: "Arimo", Arial, sans-serif; font-size: 29px; fill: var(--ink-soft); letter-spacing: 0.6px; }
  .ingredients { font-family: "Arimo", Arial, sans-serif; font-size: 16.5px; fill: var(--ink); }
  .ingredients .lead { font-weight: 700; }

  .notice { font-family: "Arimo", Arial, sans-serif; font-weight: 700; font-size: 22px; fill: var(--ink); }
  .field { font-family: "Arimo", Arial, sans-serif; font-size: 24px; fill: var(--ink); }
  .pharmacy { font-family: "Arimo", Arial, sans-serif; font-size: 23px; fill: var(--ink); }
</style>
</head>
<body>
<main class="sheet">

  <!-- Lid label, version A -->
  <svg class="label label--lid-a" viewBox="0 0 470 470" role="img" aria-label="Lid label: Velmora Skin Doctor Series Intensive eye care cream">
    <defs>
      <path id="lid-a-ring" d="M45,235 A190,190 0 1,1 425,235 A190,190 0 1,1 45,235"/>
    </defs>
    <circle class="die-cut" cx="235" cy="235" r="234"/>
    <text class="claim"><textPath href="#lid-a-ring" startOffset="122" text-anchor="middle">Doctor Formulated</textPath></text>
    <text class="claim"><textPath href="#lid-a-ring" startOffset="345" text-anchor="middle">Registered Pharmacy</textPath></text>
    <text class="claim"><textPath href="#lid-a-ring" startOffset="650" text-anchor="middle">Highest Ethical Standards</textPath></text>
    <text class="claim"><textPath href="#lid-a-ring" startOffset="1085" text-anchor="middle">Handmade</textPath></text>
    <text class="brand-name" x="235" y="432" text-anchor="middle">Velmora Skin</text>

    <text class="series" x="236" y="88" text-anchor="middle">Doctor Series</text>
    <text class="product-name" x="236" y="140" text-anchor="middle">INTENSIVE</text>
    <text class="product-type" x="231" y="170" text-anchor="middle">eye care cream</text>
    <line class="rule" x1="62" y1="193" x2="400" y2="193"/>
    <text class="ingredients" text-anchor="middle">
      <tspan x="236" y="223"><tspan class="lead">Ingredients:</tspan> Marigold extract, Witch</tspan>
      <tspan x="236" y="247">Hazel Distillate, Water, Glycerin, Stearyl</tspan>
      <tspan x="236" y="271">Alcohol, Wheat Germ Oil, Polysorbate 60,</tspan>
      <tspan x="236" y="295">Sesame Oil, Myristyl Myristate, Cetyl Alcohol,</tspan>
      <tspan x="236" y="319">Sorbitan Stearate, Phenoxyethanol,</tspan>
      <tspan x="236" y="343">Calendula Extract, Cornflower Extract,</tspan>
      <tspan x="236" y="367">Sodium Alginate, Sodium</tspan>
      <tspan x="236" y="391">Citrate, Mica, Vit. C, Vit. E.</tspan>
    </text>
  </svg>

  <!-- Base label, version A -->
  <svg class="label label--base-a" viewBox="0 0 470 470" role="img" aria-label="Base label: pharmacy details, version A">
    <circle class="die-cut" cx="235" cy="235" r="234"/>
    <text class="notice" x="233" y="55" text-anchor="middle">EXTERNAL USE</text>
    <text class="field" x="53" y="120">Rx No.</text>
    <text class="field" x="301" y="120">Date:</text>
    <text class="field" x="20" y="177">For:</text>
    <text class="field" x="343" y="177">Age:</text>
    <line class="rule" x1="3" y1="208" x2="467" y2="208"/>
    <text class="field" x="25" y="255">Pharmacist:</text>
    <text class="field" x="30" y="317">Good until:</text>
    <text class="pharmacy" text-anchor="middle">
      <tspan x="233" y="355">Pharmacy:</tspan>
      <tspan x="233" y="385">Pelaro, 18 Blvd. Ts. Orlinov,</tspan>
      <tspan x="233" y="414">Sofia 1157, ph. 02 9473615</tspan>
    </text>
  </svg>

  <!-- Lid label, version B -->
  <svg class="label label--lid-b" viewBox="0 0 470 470" role="img" aria-label="Lid label: Velmora Skin Doctor Series Intensive eye care cream">
    <defs>
      <path id="lid-b-ring" d="M45,235 A190,190 0 1,1 425,235 A190,190 0 1,1 45,235"/>
    </defs>
    <circle class="die-cut" cx="235" cy="235" r="234"/>
    <text class="claim"><textPath href="#lid-b-ring" startOffset="122" text-anchor="middle">Doctor Formulated</textPath></text>
    <text class="claim"><textPath href="#lid-b-ring" startOffset="345" text-anchor="middle">Registered Pharmacy</textPath></text>
    <text class="claim"><textPath href="#lid-b-ring" startOffset="650" text-anchor="middle">Highest Ethical Standards</textPath></text>
    <text class="claim"><textPath href="#lid-b-ring" startOffset="1085" text-anchor="middle">Handmade</textPath></text>
    <text class="brand-name" x="235" y="432" text-anchor="middle">Velmora Skin</text>

    <text class="series" x="236" y="88" text-anchor="middle">Doctor Series</text>
    <text class="product-name" x="236" y="140" text-anchor="middle">INTENSIVE</text>
    <text class="product-type" x="231" y="170" text-anchor="middle">eye care cream</text>
    <line class="rule" x1="62" y1="193" x2="400" y2="193"/>
    <text class="ingredients" text-anchor="middle">
      <tspan x="236" y="223"><tspan class="lead">Ingredients:</tspan> Marigold extract, Witch</tspan>
      <tspan x="236" y="247">Hazel Distillate, Water, Glycerin, Stearyl</tspan>
      <tspan x="236" y="271">Alcohol, Wheat Germ Oil, Polysorbate 60,</tspan>
      <tspan x="236" y="295">Sesame Oil, Myristyl Myristate, Cetyl Alcohol,</tspan>
      <tspan x="236" y="319">Sorbitan Stearate, Phenoxyethanol,</tspan>
      <tspan x="236" y="343">Calendula Extract, Cornflower Extract,</tspan>
      <tspan x="236" y="367">Sodium Alginate, Sodium</tspan>
      <tspan x="236" y="391">Citrate, Mica, Vit. C, Vit. E.</tspan>
    </text>
  </svg>

  <!-- Base label, version B -->
  <svg class="label label--base-b" viewBox="0 0 470 470" role="img" aria-label="Base label: pharmacy details, version B">
    <circle class="die-cut" cx="235" cy="235" r="234"/>
    <text class="notice" x="233" y="56" text-anchor="middle">EXTERNAL USE</text>
    <text class="pharmacy" text-anchor="middle">
      <tspan x="229" y="85">Pharmacy:</tspan>
      <tspan x="229" y="115">Pelaro, 18 Blvd. Ts. Orlinov,</tspan>
      <tspan x="229" y="145">Sofia 1157, ph. 02 9473615</tspan>
    </text>
    <line class="rule" x1="55" y1="164" x2="410" y2="164"/>
    <text class="field" x="30" y="208">For:</text>
    <text class="field" x="373" y="208">Age:</text>
    <text class="field" x="30" y="283">Rx No.</text>
    <text class="field" x="277" y="283">Date:</text>
    <text class="field" x="55" y="358">Pharmacist:</text>
    <text class="field" x="140" y="422">Good until:</text>
  </svg>

</main>
</body>
</html>
```